Plumbing Contractor Website Design

We are working with a Plumbing contractor in CA called KT Plumbline.

Some sites to use for content/competitors and inspiration:

https://www.pipevalex.com
https://www.drainmoss.com
https://quillbark.example/web/contractor/ (lots of contractor website designs we've approved and continue to show clients)

Thank you for taking the time to consider designing a website for us. We are web developers based in Stockton, CA, USA. Most of our projects go through the same process. Understanding this process may help you win a project with us. We custom-code all of our websites in-house. We don’t have any requirements as to what tools you use for your design, but we prefer Figma files. For any design that we label as four-stars, we send it to the client for review. The client picks the final design they want us to use. Once we complete this process, we will continue to show additional clients all the four-star sites and purchase them later. Your designs will have multiple chances to sell. For better chances of success, we ask that you follow these guidelines.

IMAGES:
If you use any images or icons in the design, we ask that you have a link to the asset so we can purchase the image/icon. Most of the designs we submit do not have the customer’s images on them unless they have some great images. Be creative; show us the feeling you are trying to portray with your image choices. Use any royalty-free site you choose. We subscribe to Adobe and mainly use their images, but we can purchase images outside of Adobe.

PLEASE NOTE: we will not submit designs to clients with watermarks on the images.

FONTS:
We ask that you identify the fonts used in the design. This can be done in a message if you want. We typically use Google Fonts and Adobe Fonts.

CONTENT:
We're always open to different content and ideas. We often submit designs with stock images so the client can see our vision. We typically take pictures after the website launch to use their images with our vision. Lorem Ipsum is fine for paragraphs, but we ask that you write the headers in correct English. We want to be able to show the vision and identify the sections of the website.

INSPIRATION:
We typically add a couple of links in the brief of websites we like to help you get started in your design.

REVISIONS:
We do not often ask for revisions of the designs unless we see something in the design that may not appeal to the client. If there are slight changes that we want to make, we do that in the development process.

FEEDBACK:
We rarely give feedback on designs during the design process. We are working on many website projects and do not have the time to provide feedback. We usually respond if your request is well thought out and asks specific questions, but a note asking “feedback, please” usually goes unanswered

```html
<!DOCTYPE html>
<html lang="en">
<head>
<meta charset="utf-8">
<title>Tapline Pros — Plumbing &amp; HVAC</title>
<link rel="stylesheet" href="https://fonts.googleapis.com/css2?family=Krona+One&family=Poppins:wght@400;500;600;700&display=swap">
<style>
:root{
  --blue-dark:#0b5e9c;
  --blue-deep:#08507f;
  --blue-light:#2ba6e1;
  --ink:#141414;
  --muted:#6b6b6b;
  --white:#ffffff;
  --pale:#dceef8;
  --star:#f5b301;
}
*{margin:0;padding:0;box-sizing:border-box}
html,body{width:1200px;height:4594px;overflow:hidden}
body{position:relative;background:var(--white);font-family:'Poppins',sans-serif;color:var(--ink)}
.abs{position:absolute}
.display{font-family:'Krona One',sans-serif;text-transform:uppercase;letter-spacing:.5px}
.eyebrow{font-family:'Krona One',sans-serif;font-size:16px;color:var(--blue-dark);text-transform:uppercase}
.para{font-size:13.5px;line-height:20.5px;color:var(--muted)}
.btn{display:flex;align-items:center;justify-content:center;font-weight:600;font-size:12px;text-transform:uppercase;color:var(--white);background:var(--blue-light)}
.photo{position:absolute}

/* header */
.brand{left:90px;top:14px;width:140px;height:118px;background:var(--white);border-radius:50%;display:flex;align-items:center;justify-content:center;flex-direction:column;z-index:3;box-shadow:0 0 0 4px var(--blue-dark)}
.brand-dot{width:18px;height:18px;border-radius:50%;background:var(--blue-dark);margin-bottom:6px}
.brand-name{font-family:'Poppins',sans-serif;font-weight:700;font-size:15px;color:var(--blue-dark)}
.contact-chip{display:flex;align-items:center;gap:12px;top:27px}
.chip-icon{width:42px;height:42px;background:var(--blue-light);display:flex;align-items:center;justify-content:center}
.chip-label{font-size:11px;font-weight:600;text-transform:uppercase}
.chip-value{font-family:'Krona One',sans-serif;font-size:20px;color:var(--blue-dark);letter-spacing:-.3px}
.navbar{left:0;top:93px;width:1200px;height:46px;background:var(--blue-dark)}
.nav-links{left:344px;top:93px;height:46px;display:flex;align-items:center;gap:21px;font-size:11.5px;font-weight:500;color:var(--white);text-transform:uppercase}
.nav-links .active{color:var(--blue-light)}
.quote-btn{left:972px;top:93px;width:139px;height:46px}

/* hero */
.hero{left:0;top:139px;width:1200px;height:676px;background:linear-gradient(90deg,#1d1f22 0%,#2f3338 45%,#2e5278 75%,#5a7fa3 100%)}
.hero-title{left:89px;top:345px;font-size:45px;line-height:61px;color:var(--white)}
.outline{color:transparent;-webkit-text-stroke:1.6px var(--white)}
.hero-sub{left:89px;top:545px;font-size:13.5px;font-weight:600;color:var(--white);text-transform:uppercase}
.hero-btn{left:89px;top:597px;width:177px;height:50px;border:2px solid var(--white);color:var(--white);font-weight:600;font-size:15px;display:flex;align-items:center;justify-content:center;text-transform:uppercase}
.call-box{left:763px;top:758px;width:348px;height:107px;background:var(--blue-light);display:flex;align-items:center;gap:18px;padding-left:42px;color:var(--white)}
.call-circle{width:54px;height:54px;border-radius:50%;background:var(--white);display:flex;align-items:center;justify-content:center}

/* about */
.dots{background-image:radial-gradient(var(--blue-light) 1.6px,transparent 1.8px);background-size:10px 10px}
.about-title{left:686px;top:1006px;font-size:28px;line-height:36px}

/* video */
.center-text{left:0;width:1200px;text-align:center}
.band{left:0;top:1974px;width:1200px;height:576px;background:var(--blue-dark)}
.video{left:177px;top:1601px;width:848px;height:464px;background:linear-gradient(120deg,#8c7a68 0%,#c9bfb2 40%,#6a6e72 75%,#3c4852 100%)}
.video-frame{left:171px;top:1970px;width:860px;height:98px;border:3px solid var(--white);border-top:none}
.watch{left:171px;top:1966px;width:860px;text-align:center;font-family:'Krona One',sans-serif;font-size:94px;line-height:100px;color:transparent;-webkit-text-stroke:2px var(--white);overflow:hidden;white-space:nowrap}
.play{left:545px;top:1777px;width:108px;height:108px;border-radius:50%;background:rgba(255,255,255,.55);display:flex;align-items:center;justify-content:center}

/* services */
.service{width:210px;color:var(--white)}
.service-icon{width:72px;height:70px;background:rgba(255,255,255,.18);border-radius:6px}
.service-name{font-family:'Krona One',sans-serif;font-size:19px;line-height:25px;text-transform:uppercase;margin-top:22px}
.service-arrow{width:32px;height:30px;border:1.5px solid var(--white);display:flex;align-items:center;justify-content:center;margin-top:20px}
.service-active{left:280px;top:2243px;width:210px;height:360px;background:var(--blue-light)}
.divider{width:1.5px;background:rgba(255,255,255,.6);top:2250px;height:300px}

/* team */
.member{top:3193px;width:210px;height:305px;background:linear-gradient(180deg,#c8c6c2 0%,#4a6482 60%,#1f3b5a 100%)}
.member-name{position:absolute;bottom:26px;left:0;width:100%;text-align:center;font-family:'Krona One',sans-serif;font-size:14px;color:var(--white)}

/* testimonial */
.avatar{border-radius:2px}

/* contact band */
.footer{left:0;top:4094px;width:1200px;height:500px;background:var(--blue-dark)}
.cta{left:132px;top:3994px;width:936px;height:187px;background:var(--blue-light)}
.cta-title{left:176px;top:4028px;font-size:37px;line-height:47px;color:var(--white);letter-spacing:-1px}
.cta-phone{left:842px;top:4069px;width:176px;height:34px;background:var(--white);display:flex;align-items:center;justify-content:center;gap:8px;font-weight:600;font-size:13px}
.foot-head{font-family:'Krona One',sans-serif;font-size:14px;color:var(--white);text-transform:uppercase}
.foot-list{list-style:none;font-size:13px;line-height:26.5px;color:var(--white)}
.foot-text{font-size:12.5px;line-height:21px;color:var(--white)}
.social{width:24px;height:24px;border-radius:50%;background:rgba(255,255,255,.18);display:inline-block;margin-right:8px}
</style>
</head>
<body>

<!-- header -->
<div class="abs navbar"></div>
<div class="abs brand"><span class="brand-dot"></span><span class="brand-name">Tapline Pros</span></div>

<div class="abs contact-chip" style="left:530px">
  <div class="chip-icon"><svg width="20" height="20" viewBox="0 0 24 24"><path fill="#fff" d="M6.6 10.8a15.1 15.1 0 0 0 6.6 6.6l2.2-2.2c.3-.3.7-.4 1-.2 1.1.4 2.3.6 3.6.6.6 0 1 .4 1 1V20c0 .6-.4 1-1 1A17 17 0 0 1 3 4c0-.6.4-1 1-1h3.5c.6 0 1 .4 1 1 0 1.3.2 2.5.6 3.6.1.3 0 .7-.2 1z"/></svg></div>
  <div><div class="chip-label">Call us:</div><div class="chip-value">(555) 214-7730</div></div>
</div>
<div class="abs contact-chip" style="left:811px">
  <div class="chip-icon"><svg width="20" height="16" viewBox="0 0 20 16"><path fill="#fff" d="M0 2 10 9 20 2V16H0z"/><path fill="#fff" d="M0 0h20L10 7z"/></svg></div>
  <div><div class="chip-label">Online support:</div><div class="chip-value" style="font-size:18px">hello@taplinepros.com</div></div>
</div>

<nav class="abs nav-links">
  <span class="active">Home</span><span>About Us</span><span>Services</span><span>Client Testimonials</span><span>Estimate Request</span><span>Contact Us</span>
  <svg width="14" height="14" viewBox="0 0 14 14"><circle cx="6" cy="6" r="4.5" stroke="#fff" stroke-width="1.6" fill="none"/><path d="M9.5 9.5 13 13" stroke="#fff" stroke-width="1.6"/></svg>
</nav>
<div class="abs btn quote-btn">Get a Quote</div>

<!-- hero -->
<div class="abs hero" role="img" aria-label="Plumber in cap and denim shirt checking a clipboard under a sink"></div>
<h1 class="abs display hero-title">Reliable<br><span class="outline">Plumbing</span> and<br>HVAC Solutions</h1>
<p class="abs hero-sub">Tapline Pros, we deliver expert plumbing and HVAC services</p>
<div class="abs hero-btn">Explore More</div>
<div class="abs call-box">
  <div class="call-circle"><svg width="22" height="22" viewBox="0 0 24 24"><path fill="#2ba6e1" d="M6.6 10.8a15.1 15.1 0 0 0 6.6 6.6l2.2-2.2c.3-.3.7-.4 1-.2 1.1.4 2.3.6 3.6.6.6 0 1 .4 1 1V20c0 .6-.4 1-1 1A17 17 0 0 1 3 4c0-.6.4-1 1-1h3.5c.6 0 1 .4 1 1 0 1.3.2 2.5.6 3.6.1.3 0 .7-.2 1z"/></svg></div>
  <div><div style="font-size:14px;font-weight:500">Call Us Today:</div><div style="font-family:'Krona One',sans-serif;font-size:24px">(555) 214-7730</div></div>
</div>

<!-- about -->
<div class="abs dots" style="left:478px;top:1369px;width:86px;height:82px"></div>
<div class="photo" style="left:282px;top:931px;width:362px;height:283px;background:linear-gradient(135deg,#c46a3a,#5a7790 60%,#2d3e52)" role="img" aria-label="Technician in hard hat working on a boiler"></div>
<div class="photo" style="left:89px;top:1025px;width:255px;height:253px;background:linear-gradient(135deg,#e8e8e6,#9aa5ae 60%,#3a4a5c)" role="img" aria-label="Plumber fixing a bathroom sink"></div>
<div class="photo" style="left:280px;top:1171px;width:257px;height:252px;background:linear-gradient(135deg,#dcdcdc,#41556e 55%,#273545);border:4px solid #fff" role="img" aria-label="Plumber repairing pipes under a kitchen sink"></div>
<div class="abs eyebrow" style="left:686px;top:982px">About Me</div>
<h2 class="abs display about-title">We Are Most<br>Popular Repair<br>Company</h2>
<p class="abs para" style="left:686px;top:1125px;width:392px">It is a long established fact that a reader will be distracted by the readable content of a page when looking at its layout. The point of using Lorem Ipsum is that it has a more-or-less normal distribution of letters, as opposed to using 'Content here, content here', making it look like readable English. Many desktop publishing packages and web page editors now use Lorem Ipsum as their default model text, and a search for 'lorem ipsum' will uncover many web sites still in their infancy.</p>
<div class="abs btn" style="left:686px;top:1328px;width:141px;height:50px">Read More</div>

<!-- video -->
<div class="abs eyebrow center-text" style="top:1524px">Our Video</div>
<h2 class="abs display center-text" style="top:1548px;font-size:28px">Our Best Repair Video</h2>
<div class="abs band"></div>
<div class="abs video" role="img" aria-label="Plumber adjusting a kitchen faucet"></div>
<div class="abs play"><svg width="26" height="28" viewBox="0 0 26 28"><path d="M2 1 25 14 2 27z" fill="#2ba6e1"/></svg></div>
<div class="abs watch">WATCH VID</div>
<div class="abs video-frame"></div>

<!-- services -->
<div class="abs center-text" style="top:2143px;font-family:'Krona One',sans-serif;font-size:20px;color:#fff">PROS SERVICES</div>
<h2 class="abs display center-text" style="top:2174px;font-size:29px;color:#fff">Flexible Repairing Service Work</h2>
<div class="abs service-active"></div>
<div class="abs divider" style="left:701px"></div>
<div class="abs divider" style="left:929px"></div>

<div class="abs service" style="left:100px;top:2300px">
  <div class="service-icon" role="img" aria-label="Drain pipe icon"></div>
  <div class="service-name">Drain<br>Cleaning</div>
  <div class="service-arrow"><svg width="12" height="10" viewBox="0 0 12 10"><path d="M0 5h10M6 1l4 4-4 4" stroke="#fff" stroke-width="1.3" fill="none"/></svg></div>
</div>
<div class="abs service" style="left:310px;top:2300px;width:170px">
  <div class="service-icon" role="img" aria-label="Pipe and gear icon"></div>
  <div class="service-name">Plumbing<br>Repairs</div>
  <p style="font-size:12px;line-height:20px;margin-top:14px">It is a long established fact that a reader will be distracted...</p>
  <div class="service-arrow"><svg width="12" height="10" viewBox="0 0 12 10"><path d="M0 5h10M6 1l4 4-4 4" stroke="#fff" stroke-width="1.3" fill="none"/></svg></div>
</div>
<div class="abs service" style="left:521px;top:2300px">
  <div class="service-icon" role="img" aria-label="Sewer line icon"></div>
  <div class="service-name">Sewer<br>Line Repair</div>
  <div class="service-arrow"><svg width="12" height="10" viewBox="0 0 12 10"><path d="M0 5h10M6 1l4 4-4 4" stroke="#fff" stroke-width="1.3" fill="none"/></svg></div>
</div>
<div class="abs service" style="left:731px;top:2300px">
  <div class="service-icon" role="img" aria-label="Drain grate icon"></div>
  <div class="service-name">Plumbing<br>and Drains</div>
  <div class="service-arrow"><svg width="12" height="10" viewBox="0 0 12 10"><path d="M0 5h10M6 1l4 4-4 4" stroke="#fff" stroke-width="1.3" fill="none"/></svg></div>
</div>
<div class="abs service" style="left:959px;top:2300px">
  <div class="service-icon" role="img" aria-label="Leaking valve icon"></div>
  <div class="service-name">Water<br>Damage</div>
  <div class="service-arrow"><svg width="12" height="10" viewBox="0 0 12 10"><path d="M0 5h10M6 1l4 4-4 4" stroke="#fff" stroke-width="1.3" fill="none"/></svg></div>
</div>

<!-- best plumbing -->
<h2 class="abs display" style="left:184px;top:2718px;font-size:29px;line-height:38px">Best Plumbing<br>Services</h2>
<p class="abs para" style="left:184px;top:2806px;width:395px">Is simply dummy text of the printing and typesetting industry. Lorem Ipsum has been the industry's standard dummy text ever since the 1500s, when an unknown printer took a galley of type and scrambled it to make a type specimen book. It has survived not only five centuries, but also the leap into electronic typesetting, remaining essentially unchanged. It was popularised in the 1960s with the release of Letraset sheets containing Lorem Ipsum passages, and more recently...</p>
<div class="abs btn" style="left:184px;top:3008px;width:141px;height:50px">Read More</div>
<div class="abs dots" style="left:909px;top:2978px;width:126px;height:124px"></div>
<div class="photo" style="left:645px;top:2717px;width:355px;height:355px;background:linear-gradient(135deg,#2e3f55,#8a94a0 50%,#c7ccd1);box-shadow:0 18px 30px rgba(0,0,0,.18)" role="img" aria-label="Hands tightening a chrome faucet over a steel sink"></div>

<!-- team -->
<div class="abs" style="left:0;top:3290px;width:604px;height:271px;background:var(--pale)"></div>
<div class="abs member" style="left:-106px" role="img" aria-label="Technician in overalls"><span class="member-name" style="text-align:right;padding-right:24px">Mateo</span></div>
<div class="abs member" style="left:114px" role="img" aria-label="Technician holding a wrench"><span class="member-name">Anders</span></div>
<div class="abs member" style="left:333px" role="img" aria-label="Technician sitting with tools"><span class="member-name">Corbin</span></div>
<svg class="abs" style="left:296px;top:3526px" width="40" height="16" viewBox="0 0 40 16"><path d="M6 3 1 8l5 5" stroke="#141414" stroke-width="1.4" fill="none"/><path d="M18 8h18M31 3l5 5-5 5" stroke="#141414" stroke-width="1.4" fill="none"/></svg>
<div class="abs eyebrow" style="left:665px;top:3236px">Expert Technician</div>
<h2 class="abs display" style="left:665px;top:3262px;font-size:29px;line-height:38px">Our Dedicated<br>&amp; Expert Member</h2>
<p class="abs para" style="left:665px;top:3350px;width:400px">Is simply dummy text of the printing and typesetting industry. Lorem Ipsum has been the industry's standard dummy text ever since the 1500s, when an unknown printer took a galley of type and scrambled it to make a type specimen book.</p>

<!-- testimonial -->
<svg class="abs" style="left:89px;top:3712px" width="180" height="114" viewBox="0 0 180 114"><path d="M0 114V60Q0 10 50 0l8 14Q30 24 30 50h30v64zM96 114V60q0-50 50-60l8 14q-28 10-28 36h30v64z" fill="#f1f1f1"/></svg>
<div class="abs avatar" style="left:451px;top:3662px;width:75px;height:73px;background:linear-gradient(#b39078,#5d4436)" role="img" aria-label="Client portrait"></div>
<div class="abs avatar" style="left:555px;top:3646px;width:104px;height:104px;background:linear-gradient(#8ea3ab,#3a4a52)" role="img" aria-label="Client portrait"></div>
<div class="abs avatar" style="left:686px;top:3662px;width:75px;height:73px;background:linear-gradient(#c7beb6,#6b5a4e)" role="img" aria-label="Client portrait"></div>
<p class="abs center-text" style="top:3795px;font-size:15px;line-height:24px;color:#444;padding:0 240px">Lorem Ipsum is simply dummy text of the printing and typesetting industry. Lorem Ipsum has been the industry's standard dummy text ever since the 1500s, when an unknown printer took a galley of type and scrambled it to make a type specimen ...</p>
<div class="abs center-text" style="top:3872px;color:var(--star);font-size:14px;letter-spacing:1px">★★★★★</div>
<div class="abs center-text" style="top:3900px;font-size:11.5px;font-weight:600;text-transform:uppercase">Maren Holloway</div>

<!-- contact -->
<div class="abs footer"></div>
<div class="abs cta"></div>
<h2 class="abs display cta-title">Contact Us<br>For A Free Estimate!</h2>
<p class="abs" style="left:176px;top:4131px;font-size:11.5px;font-weight:600;color:#fff;letter-spacing:-.4px">Please include year, make, and model and the service or repair you would like an estimate on.</p>
<div class="abs cta-phone"><svg width="12" height="12" viewBox="0 0 24 24"><path fill="#141414" d="M6.6 10.8a15.1 15.1 0 0 0 6.6 6.6l2.2-2.2c.3-.3.7-.4 1-.2 1.1.4 2.3.6 3.6.6.6 0 1 .4 1 1V20c0 .6-.4 1-1 1A17 17 0 0 1 3 4c0-.6.4-1 1-1h3.5c.6 0 1 .4 1 1 0 1.3.2 2.5.6 3.6.1.3 0 .7-.2 1z"/></svg>+555-318-2046</div>

<!-- footer -->
<div class="abs" style="left:107px;top:4280px;width:205px;height:160px;display:flex;flex-direction:column;align-items:center;justify-content:center;gap:10px">
  <span style="width:40px;height:40px;border-radius:50%;background:#fff;display:block"></span>
  <span style="font-weight:700;font-size:22px;color:#fff">Tapline Pros</span>
</div>
<div class="abs" style="left:387px;top:4284px">
  <div class="foot-head">Quick Link</div>
  <ul class="foot-list" style="margin-top:14px"><li>Home</li><li>About Us</li><li>Services</li><li>Client testimonials</li><li>Estimate request</li><li>Contact Us</li></ul>
</div>
<div class="abs" style="left:560px;top:4284px;width:270px">
  <div class="foot-head">Contact Us</div>
  <div class="foot-text" style="margin-top:18px;padding-left:16px;position:relative"><svg style="position:absolute;left:0;top:3px" width="9" height="12" viewBox="0 0 9 12"><path d="M4.5 0A4.5 4.5 0 0 0 0 4.5C0 8 4.5 12 4.5 12S9 8 9 4.5A4.5 4.5 0 0 0 4.5 0z" fill="#2ba6e1"/></svg>some address line goes here, city name country</div>
  <div class="foot-text" style="margin-top:4px">☏ (555) 214-7730</div>
  <div class="foot-text" style="margin-top:4px">✉ office@taplinepros.com</div>
  <div style="margin-top:14px;padding-left:2px"><span class="social"></span><span class="social"></span><span class="social"></span><span class="social"></span></div>
</div>
<div class="abs" style="left:870px;top:4284px;width:230px">
  <div class="foot-head">Newsletter</div>
  <div class="foot-text" style="margin-top:16px">It is a long established fact that a reader will be distracted .</div>
  <div style="margin-top:10px;width:221px;height:34px;background:rgba(255,255,255,.15);display:flex;align-items:center;justify-content:space-between;padding:0 14px;font-size:11px;color:#fff">✉ Enter email address <svg width="12" height="12" viewBox="0 0 12 12"><path d="M0 5 12 0 7 12 5.5 6.5z" fill="#2ba6e1"/></svg></div>
</div>
<div class="abs" style="left:96px;top:4538px;width:1010px;height:1px;background:rgba(255,255,255,.25)"></div>
<div class="abs center-text" style="top:4558px;font-size:11.5px;font-weight:500;color:#fff">© Copyright 2024 tapline pros | All Right Reserveds</div>
<div class="abs" style="left:1129px;top:4517px;width:42px;height:42px;border-radius:50%;background:var(--blue-light);display:flex;align-items:center;justify-content:center"><svg width="12" height="8" viewBox="0 0 12 8"><path d="M1 7 6 2l5 5" stroke="#fff" stroke-width="1.6" fill="none"/></svg></div>

</body>
</html>
```